Morvex Business Card (intended for Business Card sized magnet)

Hi guys,

I would like to get a design for my business card for the restaurant. The design must be single sided as I intend to produce business card sized magnets.

The File attached must me on and I'm open for new ides

Can you please ensure that the design meets Cardowell's magnetic business card size specifications:

http://www.cardowell.example.au/custom-magnets.aspx?txi=15695&xnid=TopNav_Magnetic+Business+Cards+(linked+item)_Magnets_Marketing+Products&xnav=TopNav

Full Bleed Size (starting document size):
90 x 52 mm
1062 x 615 pixels
* Finished artwork should use the full bleed dimensions for best results.

Document Trim Size (final size after being cut):
87 x 49 mm
1028 x 579 pixels
* Please be sure to keep all text within the safe margin.

Resolution:
300 DPI

The winning design/source files need to meet these specifications.

Thanks
Updates

Hi guys, can I see more options please Thanks

```html
<!DOCTYPE html>
<html lang="en">
<head>
<meta charset="utf-8">
<title>Morvex Business Card</title>
<link rel="stylesheet" href="https://fonts.googleapis.com/css2?family=EB+Garamond:wght@400&family=Lato:wght@400&display=swap">
<style>
  :root {
    --page-bg: #e6e4e0;
    --card-bg: #ebe8e2;
    --ink: #111111;
    --band-tone: #dedad3;
    --band-line: #c4c0b8;
    --ornament-tone: #5a5a5a;
  }
  html, body {
    margin: 0;
    padding: 0;
    width: 1200px;
    height: 1000px;
    overflow: hidden;
    background: var(--page-bg);
  }
  .card {
    position: absolute;
    left: 50px;
    top: 181px;
    width: 1100px;
    height: 637px;
    background: var(--card-bg);
    box-shadow: 0 2px 10px rgba(0,0,0,0.12);
    overflow: hidden;
  }
  .pattern-band {
    position: absolute;
    left: 0;
    width: 100%;
    height: 100px;
    background: linear-gradient(90deg, #ddd8d0, #e1ddd6 50%, #ddd8d0);
  }
  .pattern-band--top { top: 0; border-bottom: 3px solid var(--band-line); }
  .pattern-band--bottom { bottom: 0; height: 110px; border-top: 3px solid var(--band-line); }
  .wordmark {
    position: absolute;
    left: 0;
    width: 100%;
    top: 62px;
    text-align: center;
    font-family: "EB Garamond", Georgia, serif;
    font-weight: 400;
    font-size: 118px;
    line-height: 1;
    color: var(--ink);
    margin: 0;
  }
  .ornament-frame {
    position: absolute;
    left: 322px;
    top: 200px;
    width: 472px;
    height: 158px;
  }
  .ornament-rule {
    position: absolute;
    left: 0;
    width: 100%;
    height: 4px;
    background: var(--ink);
  }
  .ornament-rule--top { top: 0; }
  .ornament-rule--bottom { bottom: 0; }
  .ornament-strip {
    position: absolute;
    left: 0;
    top: 14px;
    width: 100%;
    height: 130px;
    background: linear-gradient(90deg, #6a6a6a, #4e4e4e 50%, #6a6a6a);
  }
  .contact {
    position: absolute;
    left: 0;
    width: 100%;
    top: 386px;
    text-align: center;
    font-family: "Lato", "Gill Sans", Arial, sans-serif;
    font-weight: 400;
    color: var(--ink);
    font-size: 31px;
    line-height: 1;
    margin: 0;
    padding: 0;
    list-style: none;
  }
  .contact li { margin-bottom: 21px; }
</style>
</head>
<body>
  <article class="card">
    <div class="pattern-band pattern-band--top" role="img" aria-label="Faint repeating geometric star-tile border in soft grey with pastel accents"></div>

    <h1 class="wordmark">Morvex</h1>

    <div class="ornament-frame">
      <div class="ornament-rule ornament-rule--top"></div>
      <div class="ornament-strip" role="img" aria-label="Black interlaced geometric star ornament band with red, blue and yellow centres"></div>
      <div class="ornament-rule ornament-rule--bottom"></div>
    </div>

    <ul class="contact">
      <li class="contact-address">214 Larkfield Rd, Brenwood East 3190</li>
      <li class="contact-phone">039 5501 2843</li>
      <li class="contact-web">www.morvex.com.au</li>
      <li class="contact-email">hello@morvex.example.au</li>
    </ul>

    <div class="pattern-band pattern-band--bottom" role="img" aria-label="Faint repeating geometric star-tile border in soft grey with pastel accents" style="z-index:0"></div>
  </article>
  <style>.contact{z-index:1}</style>
</body>
</html>
```